Book Cover : Silent Tides: Protein Engines and the Cellular Horizon

We need a striking and engaging book cover for this new book which describes the development of the COVID-19 vaccine technology and it's potential to change the world in ways which most people don't yet realise.

On the book cover we need to include:

Silent Tides: Protein Engines and the Cellular Horizon

Safety/Efficiency/Future Applications/CRISPR

Tadeusz Głowik

Need extra days to review

```html
<!DOCTYPE html>
<html lang="en">
<head>
<meta charset="utf-8">
<title>Silent Tides – Book Cover</title>
<link rel="stylesheet" href="https://fonts.googleapis.com/css2?family=Source+Sans+3:ital,wght@0,400;0,600;0,700;1,400;1,700&display=swap">
<style>
  :root {
    --page: #ffffff;
    --paper: #ffffff;
    --ink: #1a1a1a;
    --red: #c8060c;
    --art-light: #f4f1f1;
    --art-mid: #e6b7b5;
    --art-deep: #a8141c;
  }
  * { margin: 0; padding: 0; box-sizing: border-box; }
  html, body {
    width: 1200px; height: 1200px; overflow: hidden;
    background: var(--page);
    font-family: "Source Sans 3", Arial, sans-serif;
    color: var(--ink);
  }
  .canvas { position: relative; width: 1200px; height: 1200px; overflow: hidden; }
  .spread {
    position: absolute; left: 0; top: 165px;
    width: 1200px; height: 870px;
    background: var(--paper);
    box-shadow: 0 0 22px rgba(0,0,0,0.35);
    overflow: hidden;
  }
  /* Back cover */
  .back { position: absolute; left: 0; top: 0; width: 581px; height: 870px; }
  .blurb {
    position: absolute; left: 76px; top: 86px; width: 428px;
    font-size: 17.5px; line-height: 25.5px; text-align: center; letter-spacing: -0.2px;
  }
  .divider {
    position: absolute; left: 0; width: 581px; top: 214px;
    text-align: center; font-size: 12px; letter-spacing: 1px;
  }
  .about-title {
    position: absolute; left: 77px; width: 428px; top: 230px;
    text-align: center; color: var(--red);
    font-size: 30px; font-weight: 700; font-style: italic; letter-spacing: -0.5px;
  }
  .bio {
    position: absolute; left: 77px; top: 274px; width: 425px;
    font-size: 17.5px; line-height: 25.5px; text-align: justify; letter-spacing: -0.2px;
  }
  .bio p { margin-bottom: 25px; }
  .bio em { font-weight: 700; }
  /* Spine */
  .spine {
    position: absolute; left: 581px; top: 0; width: 38px; height: 870px;
    background: var(--red); overflow: hidden;
  }
  .spine-text {
    position: absolute; left: 19px; top: 255px;
    transform-origin: 0 0; transform: rotate(90deg) translateY(-50%);
    white-space: nowrap; color: #fff;
    display: flex; align-items: baseline; width: 585px;
  }
  .spine-title { font-size: 20px; font-weight: 600; letter-spacing: -0.3px; }
  .spine-subtitle { font-size: 14px; margin-left: 8px; }
  .spine-author { font-size: 22px; margin-left: auto; }
  /* Front cover */
  .front { position: absolute; left: 619px; top: 0; width: 581px; height: 870px; overflow: hidden; }
  .cover-art {
    position: absolute; left: 0; top: 0; width: 581px; height: 395px;
    background:
      radial-gradient(ellipse 170px 150px at 420px 200px, var(--art-deep) 0%, var(--art-mid) 55%, rgba(255,255,255,0) 100%),
      radial-gradient(ellipse 60px 80px at 120px 290px, #e9cf6a 0%, rgba(255,255,255,0) 100%),
      linear-gradient(180deg, #fff 0%, var(--art-light) 60%, #fff 100%);
  }
  .title {
    position: absolute; left: 0; width: 581px; top: 388px;
    text-align: center; color: var(--red); font-weight: 600;
    letter-spacing: -2px; line-height: 0.9;
  }
  .title .line-a { display: block; font-size: 86px; }
  .title .line-b { display: block; font-size: 94px; }
  .subtitle {
    position: absolute; left: 0; width: 581px; top: 638px;
    text-align: center; font-size: 38px; letter-spacing: -0.6px; color: var(--ink);
  }
  .topics {
    position: absolute; left: 0; width: 581px; top: 700px;
    text-align: center; font-size: 22px; letter-spacing: -0.3px;
  }
  .author-band {
    position: absolute; left: 0; top: 765px; width: 581px; height: 78px;
    background: var(--red); color: #fff;
    display: flex; align-items: center; justify-content: center;
    font-size: 44px; letter-spacing: -0.5px;
  }
</style>
</head>
<body>
<div class="canvas">
  <div class="spread">
    <section class="back">
      <p class="blurb">The COVID-19 vaccines. How do they work? How are they different to traditional vaccines? How can the technology they’re based on change the world in very surprising ways? All clearly explained in this new and exciting book.</p>
      <div class="divider">***</div>
      <h2 class="about-title">About the Author</h2>
      <div class="bio">
        <p><em>Tadeusz Głowik</em> is a Polish scientist who has studied and worked in molecular genetics. He studied Chemistry at the Vistula Polytechnic and Biological Chemistry at the University of Calderbridge. He also holds an MBA which he completed with Distinction. He is a member of the Lumen Society.</p>
        <p>He has been a publisher, a writer, a teacher, a corporate presenter, a forensic scientist for the Police force, and a scientific researcher.</p>
        <p>His comprehensive knowledge of genetics, biochemistry, biology, chemistry and physics, as well as teaching effectiveness and quality, helped him win The Best Teacher Award in 2006.</p>
        <p>He is passionate and devoted to making people aware of new scientific technologies.</p>
      </div>
    </section>

    <div class="spine">
      <div class="spine-text">
        <span class="spine-title">Silent Tides</span>
        <span class="spine-subtitle">Protein Engines and the Cellular Horizon</span>
        <span class="spine-author">Tadeusz Głowik</span>
      </div>
    </div>

    <section class="front">
      <div class="cover-art" role="img" aria-label="Illustration of a syringe injecting a red spiked virus particle that breaks apart, with a small vaccine vial of yellow liquid beside it"></div>
      <h1 class="title">
        <span class="line-a">Silent Tides:</span>
        <span class="line-b">Protein</span>
        <span class="line-b">Engines</span>
      </h1>
      <p class="subtitle">and the Cellular Horizon</p>
      <p class="topics">Safety/Efficiency/Future Applications/CRISPR</p>
      <div class="author-band">Tadeusz Głowik</div>
    </section>
  </div>
</div>
</body>
</html>
```